Label Project

We need a new label design for a product (Tactile Workflow Layout Planner Kit) that is used for training purpose.

Product Dimensions: 18 x 3.5 x 13 inches ; 6.4 pounds (pictures attached)

Target Market(s)

Lean Six Sigma practitioners

Industry/Entity Type

Training

Requirements
Must have
• Company logo (file is attached)

```html
<!DOCTYPE html>
<html lang="en">
<head>
<meta charset="utf-8">
<title>Tactile Workflow Layout Planner Kit – Label</title>
<link href="https://fonts.googleapis.com/css2?family=Saira+Semi+Condensed:wght@400;700;800&display=swap" rel="stylesheet">
<style>
  :root {
    --hazard-dark: #111111;
    --hazard-light: #ffffff;
    --label-yellow: #ffee00;
    --label-yellow-soft: #f6e21a;
    --ink: #111111;
    --strip-white: #ffffff;
  }
  html, body {
    margin: 0;
    padding: 0;
    width: 1200px;
    height: 673px;
    overflow: hidden;
    background: #ffffff;
  }
  .label {
    position: relative;
    width: 1200px;
    height: 673px;
    overflow: hidden;
    background: repeating-linear-gradient(
      -45deg,
      var(--hazard-dark) 0 9px,
      var(--hazard-light) 9px 20px
    );
    font-family: "Saira Semi Condensed", "Arial Narrow", sans-serif;
    color: var(--ink);
  }
  .brand-strip {
    position: absolute;
    left: 28px;
    top: 30px;
    width: 102px;
    height: 613px;
    background: var(--strip-white);
  }
  .brand-name {
    position: absolute;
    left: 51px;
    top: 235px;
    transform: translate(-50%, -50%) rotate(-90deg);
    white-space: nowrap;
    font-weight: 400;
    font-size: 38px;
    letter-spacing: 1px;
    line-height: 1;
  }
  .brand-mark {
    position: absolute;
    left: 31px;
    top: 522px;
    width: 42px;
    height: 42px;
    border-radius: 50%;
    background: var(--ink);
  }
  .panel {
    position: absolute;
    left: 130px;
    top: 30px;
    width: 1046px;
    height: 613px;
    background: var(--label-yellow);
  }
  .panel-backdrop {
    position: absolute;
    inset: 0;
    background: radial-gradient(ellipse at 55% 55%, var(--label-yellow) 0%, var(--label-yellow-soft) 100%);
  }
  .title {
    position: absolute;
    left: 0;
    right: 0;
    top: 38px;
    margin: 0;
    text-align: center;
    font-weight: 800;
    font-size: 88px;
    line-height: 104px;
    letter-spacing: 2px;
    text-transform: uppercase;
  }
  .features {
    position: absolute;
    left: 38px;
    top: 304px;
    margin: 0;
    padding: 0;
    list-style: none;
    font-weight: 700;
    font-size: 30px;
    line-height: 50px;
  }
  .feature {
    display: grid;
    grid-template-columns: 44px 94px auto;
    align-items: start;
  }
  .feature-arrow {
    width: 22px;
    height: 22px;
    margin-top: 14px;
  }
  .feature-count { letter-spacing: 1px; }
  .feature-text { text-transform: uppercase; letter-spacing: 1px; }
  .feature-text .mixed { text-transform: none; }
</style>
</head>
<body>
<div class="label">
  <aside class="brand-strip">
    <span class="brand-name">HALDEN WORKS</span>
    <span class="brand-mark"></span>
  </aside>

  <main class="panel">
    <div class="panel-backdrop" role="img" aria-label="Faint value stream mapping icons — trucks, process boxes, push arrows and cycle loops — spread across the yellow background"></div>

    <h1 class="title">Tactile Workflow<br>Layout Planner Kit</h1>

    <ul class="features">
      <li class="feature">
        <svg class="feature-arrow" viewBox="0 0 22 22" aria-hidden="true"><path d="M2 2 L20 11 L2 20 L7 11 Z" fill="#111"/></svg>
        <span class="feature-count">240</span>
        <span class="feature-text">Magnetic Icons</span>
      </li>
      <li class="feature">
        <svg class="feature-arrow" viewBox="0 0 22 22" aria-hidden="true"><path d="M2 2 L20 11 L2 20 L7 11 Z" fill="#111"/></svg>
        <span class="feature-count">17</span>
        <span class="feature-text">Unique Symbols to Materials and<br>Information Flow</span>
      </li>
      <li class="feature">
        <svg class="feature-arrow" viewBox="0 0 22 22" aria-hidden="true"><path d="M2 2 L20 11 L2 20 L7 11 Z" fill="#111"/></svg>
        <span class="feature-count">2</span>
        <span class="feature-text">Lean Six Sigma Deployment Field<br><span class="mixed">Guide ® Handbook</span></span>
      </li>
    </ul>
  </main>
</div>
</body>
</html>
```